One page sales fact sheet for data consultancy company

We need a serious and professional looking 1-page fact sheet that we want to send over to potential clients via email.
The upper part should consists of a header, the client logo and 3 charts.
(1 chart with 5 datapoints / 1 chart with 3 bubbles and percentage in it, 1 chart with numbers and text)
In the lower part there should be some text description about our company and a big chart consisting of a table (see drawing).
See attached drawing to get a better understanding of the whole idea.
The fact sheet should be catchy but professional in the same way.
Colors your choice but classic, i.e. black/white/grey/blue
The contest winner can expect more work from us based on the winning design.
*Please note that the logo reflects our original logo style but is not our
actual company name for privacy reasons

```html
<!DOCTYPE html>
<html lang="en">
<head>
<meta charset="utf-8">
<title>Market Analysis Fact Sheet</title>
<link rel="stylesheet" href="https://fonts.googleapis.com/css2?family=Montserrat:wght@400;500;600;700;800&display=swap">
<style>
:root{
  --teal:#15607c;
  --grey:#c6c6c6;
  --grey-light:#e3e3e3;
  --grey-row:#ececec;
  --grey-mid:#a6a6a6;
  --dark:#333333;
  --ink:#111111;
  --text:#3b3b3b;
  --muted:#8a8a8a;
  --paper:#ffffff;
}
*{margin:0;padding:0;box-sizing:border-box}
html,body{width:894px;height:1200px;overflow:hidden;background:var(--paper)}
body{font-family:"Montserrat",Arial,sans-serif;color:var(--text)}
.sheet{position:relative;width:894px;height:1200px;background:var(--paper)}
.abs{position:absolute}

.header{left:0;top:0;width:894px;height:85px;background:var(--teal);color:#fff}
.header-title{position:absolute;left:25px;top:24px;font-size:30px;font-weight:700;letter-spacing:.3px}
.header-title b{font-weight:800}
.header-date{position:absolute;right:26px;top:33px;font-size:22px;font-weight:600}

.brand{left:0;top:100px;width:894px;text-align:center;font-size:70px;font-weight:800;color:var(--ink);letter-spacing:1px;line-height:80px}

.chart-title{font-size:16px;font-weight:500;color:var(--ink)}
.chart-title b{font-weight:700}
.chart{width:258px;height:136px}
.chart text{font-family:"Montserrat",Arial,sans-serif;font-size:6px;fill:#666}

.bullets{left:31px;top:408px;width:280px;list-style:none}
.bullets li{position:relative;padding-left:22px;font-size:10.5px;font-weight:500;line-height:13.5px;color:var(--ink);height:76.5px}
.bullets li svg{position:absolute;left:0;top:3px}

.ring{width:120px;height:120px}
.product{width:130px}
.product-name{font-size:10px;font-weight:700;letter-spacing:.5px}
.product-desc{font-size:8.5px;line-height:10.5px;color:var(--muted);margin-top:5px;width:120px}

.stat{left:636px;width:230px}
.stat-line{padding-left:2px;color:var(--ink);font-weight:700;font-size:18px;white-space:nowrap}
.stat-line small{font-size:9px;font-weight:700;letter-spacing:.3px}
.stat-line small.low{text-transform:none;font-weight:600}
.stat-track{margin-top:6px;height:5px;border-radius:3px;background:var(--grey-light);overflow:hidden}
.stat-fill{height:100%;background:var(--teal);border-radius:3px}

.testimonial{left:636px;top:656px;width:230px;height:102px;background:#f0f0f0;border-radius:12px;text-align:center}
.testimonial-title{margin-top:14px;font-size:10px;font-weight:700;color:var(--teal);letter-spacing:.5px}
.testimonial-text{margin:10px auto 0;width:180px;font-size:10.5px;line-height:13px;color:var(--dark);font-weight:500}
.quote{position:absolute;font-size:34px;font-weight:800;color:var(--grey-mid);font-style:normal;line-height:1}
.quote.open{left:14px;top:12px}
.quote.close{right:14px;top:70px}

.section-head{top:792px;display:flex;align-items:center;gap:8px;font-size:16.5px;font-weight:600;color:var(--ink)}
.section-head b{font-weight:700}
.section-head .sep{font-weight:500}
.section-body{top:834px;width:250px;font-size:10.5px;line-height:19.5px;color:var(--teal);font-weight:500}

.data-table{left:39px;top:987px;border-collapse:separate;border-spacing:2px 2px;font-size:10.5px;text-align:center;margin-left:-2px}
.data-table th{height:18px;font-weight:600;color:#fff;background:var(--teal)}
.data-table th.alt{background:var(--grey);color:var(--dark)}
.data-table th.blank{background:transparent}
.data-table td{height:20px;background:var(--grey-row);color:var(--dark);font-weight:500}
.data-table tr:nth-child(even) td{background:#e2e2e2}
.data-table td.row-head{background:var(--teal)!important;color:#fff;font-weight:600}

.footer{left:0;top:1184px;width:894px;height:16px;background:var(--teal);color:#fff;font-size:7.5px;font-weight:700;text-align:center;line-height:16px}
</style>
</head>
<body>
<div class="sheet">

  <header class="abs header">
    <h1 class="header-title"><b>MARKET ANALYSIS</b> FACT SHEET</h1>
    <div class="header-date">June, 2020</div>
  </header>

  <div class="abs brand">VORTA</div>

  <!-- Chart 01 -->
  <h2 class="abs chart-title" style="left:21px;top:208px"><b>CHART 01</b> title</h2>
  <svg class="abs chart" style="left:19px;top:238px" viewBox="0 0 258 136">
    <g stroke="#e6e6e6" stroke-width=".6">
      <line x1="22" y1="6" x2="256" y2="6"/><line x1="22" y1="24.7" x2="256" y2="24.7"/>
      <line x1="22" y1="43.3" x2="256" y2="43.3"/><line x1="22" y1="62" x2="256" y2="62"/>
      <line x1="22" y1="80.7" x2="256" y2="80.7"/><line x1="22" y1="99.3" x2="256" y2="99.3"/>
      <line x1="22" y1="118" x2="256" y2="118" stroke="#bbb"/>
    </g>
    <g text-anchor="end">
      <text x="14" y="8">120</text><text x="14" y="26.7">100</text><text x="14" y="45.3">80</text>
      <text x="14" y="64">60</text><text x="14" y="82.7">40</text><text x="14" y="101.3">20</text><text x="14" y="120">0</text>
    </g>
    <g fill="var(--teal)">
      <rect x="31" y="24.7" width="9" height="93.3"/><rect x="63.9" y="34" width="9" height="84"/>
      <rect x="96.7" y="71.3" width="9" height="46.7"/><rect x="129.6" y="24.7" width="9" height="93.3"/>
      <rect x="162.4" y="24.7" width="9" height="93.3"/><rect x="195.3" y="62" width="9" height="56"/>
      <rect x="228.1" y="71.3" width="9" height="46.7"/>
    </g>
    <g fill="var(--grey)">
      <rect x="41" y="34" width="9" height="84"/><rect x="73.9" y="43.3" width="9" height="74.7"/>
      <rect x="106.7" y="24.7" width="9" height="93.3"/><rect x="139.6" y="62" width="9" height="56"/>
      <rect x="172.4" y="34" width="9" height="84"/><rect x="205.3" y="48" width="9" height="70"/>
      <rect x="238.1" y="24.7" width="9" height="93.3"/>
    </g>
    <g text-anchor="middle">
      <text x="40" y="130">Sun</text><text x="73" y="130">Mon</text><text x="106" y="130">Tu</text>
      <text x="139" y="130">We</text><text x="171" y="130">Th</text><text x="204" y="130">Fr</text><text x="237" y="130">Sa</text>
    </g>
  </svg>

  <!-- Chart 02 -->
  <h2 class="abs chart-title" style="left:318px;top:207px"><b>CHART 02</b> title</h2>
  <svg class="abs chart" style="left:317px;top:238px" viewBox="0 0 258 136">
    <g stroke="#e6e6e6" stroke-width=".6">
      <line x1="22" y1="6" x2="250" y2="6"/><line x1="22" y1="24.7" x2="250" y2="24.7"/>
      <line x1="22" y1="43.3" x2="250" y2="43.3"/><line x1="22" y1="62" x2="250" y2="62"/>
      <line x1="22" y1="80.7" x2="250" y2="80.7"/><line x1="22" y1="99.3" x2="250" y2="99.3"/>
      <line x1="22" y1="118" x2="250" y2="118" stroke="#bbb"/>
    </g>
    <g text-anchor="end">
      <text x="14" y="8">120</text><text x="14" y="26.7">100</text><text x="14" y="45.3">80</text>
      <text x="14" y="64">60</text><text x="14" y="82.7">40</text><text x="14" y="101.3">20</text><text x="14" y="120">0</text>
    </g>
    <polyline fill="none" stroke="var(--grey)" stroke-width="2" points="50.5,34 79,43.3 107.5,24.7 136,62 164.5,34 193,48 221.5,24.7"/>
    <g fill="var(--grey)">
      <rect x="47.5" y="31" width="6" height="6"/><rect x="76" y="40.3" width="6" height="6"/><rect x="104.5" y="21.7" width="6" height="6"/>
      <rect x="133" y="59" width="6" height="6"/><rect x="161.5" y="31" width="6" height="6"/><rect x="190" y="45" width="6" height="6"/><rect x="218.5" y="21.7" width="6" height="6"/>
    </g>
    <polyline fill="none" stroke="var(--teal)" stroke-width="2" points="50.5,24.7 79,34 107.5,71.3 136,24.7 164.5,24.7 193,62 221.5,71.3"/>
    <g fill="var(--teal)">
      <path d="M50.5 21l3.7 3.7-3.7 3.7-3.7-3.7z"/><path d="M79 30.3l3.7 3.7-3.7 3.7-3.7-3.7z"/><path d="M107.5 67.6l3.7 3.7-3.7 3.7-3.7-3.7z"/>
      <path d="M136 21l3.7 3.7-3.7 3.7-3.7-3.7z"/><path d="M164.5 21l3.7 3.7-3.7 3.7-3.7-3.7z"/><path d="M193 58.3l3.7 3.7-3.7 3.7-3.7-3.7z"/><path d="M221.5 67.6l3.7 3.7-3.7 3.7-3.7-3.7z"/>
    </g>
    <g text-anchor="middle">
      <text x="22" y="130">0</text><text x="50.5" y="130">1</text><text x="79" y="130">2</text><text x="107.5" y="130">3</text>
      <text x="136" y="130">4</text><text x="164.5" y="130">5</text><text x="193" y="130">6</text><text x="221.5" y="130">7</text><text x="250" y="130">8</text>
    </g>
  </svg>

  <!-- Chart 03 -->
  <h2 class="abs chart-title" style="left:616px;top:207px"><b>CHART 03</b> title</h2>
  <svg class="abs chart" style="left:617px;top:238px" viewBox="0 0 258 136">
    <line x1="26" y1="4" x2="26" y2="120" stroke="#bbb" stroke-width=".6"/>
    <line x1="250" y1="4" x2="250" y2="120" stroke="#e6e6e6" stroke-width=".6"/>
    <g text-anchor="end">
      <text x="20" y="14">Sa</text><text x="20" y="31">Fr</text><text x="20" y="48">Th</text><text x="20" y="65">We</text>
      <text x="20" y="82">Tu</text><text x="20" y="99">Mon</text><text x="20" y="116">Sun</text>
    </g>
    <g fill="var(--grey)">
      <rect x="82" y="8.5" width="112" height="7"/><rect x="93.2" y="25.5" width="84" height="7"/>
      <rect x="138" y="42.5" width="100.8" height="7"/><rect x="138" y="59.5" width="67.2" height="7"/>
      <rect x="82" y="76.5" width="112" height="7"/><rect x="126.8" y="93.5" width="89.6" height="7"/>
      <rect x="138" y="110.5" width="100.8" height="7"/>
    </g>
    <g fill="var(--teal)">
      <rect x="26" y="8.5" width="56" height="7"/><rect x="26" y="25.5" width="67.2" height="7"/>
      <rect x="26" y="42.5" width="112" height="7"/><rect x="26" y="59.5" width="112" height="7"/>
      <rect x="26" y="76.5" width="56" height="7"/><rect x="26" y="93.5" width="100.8" height="7"/>
      <rect x="26" y="110.5" width="112" height="7"/>
    </g>
    <g text-anchor="middle" style="font-size:5.5px">
      <g style="fill:#fff">
        <text x="54" y="14">50</text><text x="59.6" y="31">60</text><text x="82" y="48">100</text><text x="82" y="65">100</text>
        <text x="54" y="82">50</text><text x="76.4" y="99">90</text><text x="82" y="116">100</text>
      </g>
      <g style="fill:#555">
        <text x="138" y="14">100</text><text x="135.2" y="31">75</text><text x="188.4" y="48">90</text><text x="171.6" y="65">60</text>
        <text x="138" y="82">100</text><text x="171.6" y="99">80</text><text x="188.4" y="116">90</text>
      </g>
    </g>
    <g text-anchor="middle">
      <text x="26" y="130">0</text><text x="82" y="130">50</text><text x="138" y="130">100</text><text x="194" y="130">150</text><text x="250" y="130">200</text>
    </g>
  </svg>

  <!-- Bullet points -->
  <ul class="abs bullets">
    <li><svg width="8" height="8" viewBox="0 0 8 8"><path d="M1 0l6 4-6 4 2-4z" fill="var(--ink)"/></svg>Lorem Ipsum is simply dummy text of the printing and typesetting industry.</li>
    <li><svg width="8" height="8" viewBox="0 0 8 8"><path d="M1 0l6 4-6 4 2-4z" fill="var(--ink)"/></svg>Lorem Ipsum is simply dummy text of the printing and typesetting industry.</li>
    <li><svg width="8" height="8" viewBox="0 0 8 8"><path d="M1 0l6 4-6 4 2-4z" fill="var(--ink)"/></svg>Lorem Ipsum is simply dummy text of the printing and typesetting industry.</li>
    <li><svg width="8" height="8" viewBox="0 0 8 8"><path d="M1 0l6 4-6 4 2-4z" fill="var(--ink)"/></svg>Lorem Ipsum is simply dummy text of the printing and typesetting industry.</li>
    <li><svg width="8" height="8" viewBox="0 0 8 8"><path d="M1 0l6 4-6 4 2-4z" fill="var(--ink)"/></svg>Lorem Ipsum is simply dummy text of the printing and typesetting industry.</li>
  </ul>

  <!-- Percentage rings -->
  <svg class="abs ring" style="left:322px;top:392px" viewBox="0 0 120 120">
    <circle cx="60" cy="60" r="57" fill="#fff" stroke="#efefef" stroke-width="3"/>
    <circle cx="60" cy="60" r="48" fill="none" stroke="var(--grey-light)" stroke-width="5"/>
    <circle cx="60" cy="60" r="48" fill="none" stroke="var(--teal)" stroke-width="5" stroke-dasharray="220 302" transform="rotate(-90 60 60)"/>
    <text x="61" y="68" text-anchor="middle" style="font-family:Montserrat,Arial,sans-serif;font-size:24px;font-weight:700;fill:var(--teal)">73%</text>
  </svg>
  <div class="abs product" style="left:462px;top:424px">
    <div class="product-name" style="color:var(--teal)">PRODUCT TYPE 01</div>
    <p class="product-desc">Lorem Ipsum is simply dummy text of the printing and typesetting industry.</p>
  </div>

  <svg class="abs ring" style="left:322px;top:521px" viewBox="0 0 120 120">
    <circle cx="60" cy="60" r="57" fill="#fff" stroke="#efefef" stroke-width="3"/>
    <circle cx="60" cy="60" r="48" fill="none" stroke="var(--grey-light)" stroke-width="5"/>
    <circle cx="60" cy="60" r="48" fill="none" stroke="var(--grey-mid)" stroke-width="5" stroke-dasharray="151 302" transform="rotate(-90 60 60) scale(1 -1) translate(0 -120)"/>
    <text x="61" y="68" text-anchor="middle" style="font-family:Montserrat,Arial,sans-serif;font-size:24px;font-weight:700;fill:var(--grey-mid)">50%</text>
  </svg>
  <div class="abs product" style="left:461px;top:552px">
    <div class="product-name" style="color:var(--grey-mid)">PRODUCT TYPE 02</div>
    <p class="product-desc">Lorem Ipsum is simply dummy text of the printing and typesetting industry.</p>
  </div>

  <svg class="abs ring" style="left:322px;top:648px" viewBox="0 0 120 120">
    <circle cx="60" cy="60" r="57" fill="#fff" stroke="#efefef" stroke-width="3"/>
    <circle cx="60" cy="60" r="48" fill="none" stroke="var(--grey-light)" stroke-width="5"/>
    <circle cx="60" cy="60" r="48" fill="none" stroke="var(--dark)" stroke-width="5" stroke-dasharray="75 302" transform="rotate(180 60 60)"/>
    <text x="61" y="68" text-anchor="middle" style="font-family:Montserrat,Arial,sans-serif;font-size:24px;font-weight:700;fill:var(--dark)">25%</text>
  </svg>
  <div class="abs product" style="left:465px;top:681px">
    <div class="product-name" style="color:var(--dark)">PRODUCT TYPE 03</div>
    <p class="product-desc">Lorem Ipsum is simply dummy text of the printing and typesetting industry.</p>
  </div>

  <!-- Key figures -->
  <div class="abs stat" style="top:408px">
    <div class="stat-line">20 <small>PRODUCTION</small></div>
    <div class="stat-track"><div class="stat-fill" style="width:20%"></div></div>
  </div>
  <div class="abs stat" style="top:472px">
    <div class="stat-line">450 <small>PRODUCTS</small></div>
    <div class="stat-track"><div class="stat-fill" style="width:64%"></div></div>
  </div>
  <div class="abs stat" style="top:535px">
    <div class="stat-line">330,000 <small class="low">available items</small></div>
    <div class="stat-track"><div class="stat-fill" style="width:40%"></div></div>
  </div>
  <div class="abs stat" style="top:599px">
    <div class="stat-line">40Mn <small class="low">in sales</small></div>
    <div class="stat-track"><div class="stat-fill" style="width:85%"></div></div>
  </div>

  <aside class="abs testimonial">
    <span class="quote open">&ldquo;</span>
    <div class="testimonial-title">SP. TESTIMONIAL</div>
    <p class="testimonial-text">Lorem Ipsum is simply dummy text of the printing and typesetting industry.</p>
    <span class="quote close">&rdquo;</span>
  </aside>

  <!-- Company sections -->
  <h3 class="abs section-head" style="left:27px">
    <svg width="28" height="26" viewBox="0 0 28 26" fill="none" stroke="var(--ink)" stroke-width="1.6">
      <circle cx="6" cy="5" r="2.5"/><circle cx="14" cy="4" r="2.8"/><circle cx="22" cy="5" r="2.5"/>
      <path d="M3 24V11q0-2 3-2t3 2v13M11 24V10q0-2.5 3-2.5t3 2.5v14M19 24V11q0-2 3-2t3 2v13"/>
    </svg>
    <span class="sep">|</span> <b>ABOUT US</b>
  </h3>
  <p class="abs section-body" style="left:31px">Lorem ipsum dolor sit amet, consectetuer adipiscing elit, sed diam nonummy nibh euismod tincidunt ut laoreet dolore magna aliquam erat volutpat. Ut wisi enim ad minim veniam, quis nostrud exerci tation ullamcorper suscipit lobortis nisl ut aliquip ex ea commodo consequat.</p>

  <h3 class="abs section-head" style="left:324px">
    <svg width="28" height="26" viewBox="0 0 28 26" fill="none" stroke="var(--ink)" stroke-width="1.6">
      <circle cx="13" cy="14" r="11"/><circle cx="13" cy="14" r="7"/><circle cx="13" cy="14" r="3"/>
      <path d="M13 14L25 3M21 3h4v4"/>
    </svg>
    <span class="sep">|</span> <b>MISSION</b>&nbsp;&amp;&nbsp;<b>VISION</b>
  </h3>
  <p class="abs section-body" style="left:324px">Lorem ipsum dolor sit amet, consectetuer adipiscing elit, sed diam nonummy nibh euismod tincidunt ut laoreet dolore magna aliquam erat volutpat. Ut wisi enim ad minim veniam, quis nostrud exerci tation ullamcorper suscipit lobortis nisl ut aliquip ex ea commodo consequat.</p>

  <h3 class="abs section-head" style="left:610px">
    <svg width="28" height="26" viewBox="0 0 28 26" fill="none" stroke="var(--ink)" stroke-width="1.6">
      <path d="M10 17l-3-3L17 4q5-3 8-3-0 3-3 8L12 19z"/><circle cx="18.5" cy="8.5" r="2"/>
      <path d="M8 12l-4 0-3 3 5 1M14 18l0 4-3 3-1-5M6 20l-4 4"/>
    </svg>
    <span class="sep">|</span> <b>PRODUCTS/SERVICES</b>
  </h3>
  <p class="abs section-body" style="left:617px">Lorem ipsum dolor sit amet, consectetuer adipiscing elit, sed diam nonummy nibh euismod tincidunt ut laoreet dolore magna aliquam erat volutpat. Ut wisi enim ad minim veniam, quis nostrud exerci tation ullamcorper suscipit lobortis nisl ut aliquip ex ea commodo consequat.</p>

  <!-- Data table -->
  <table class="abs data-table">
    <thead>
      <tr>
        <th class="blank" style="width:164px"></th>
        <th style="width:163px">Title here</th>
        <th class="alt" style="width:116px">Numbers</th>
        <th style="width:104px">Value</th>
        <th class="alt" style="width:128px">Brand</th>
        <th style="width:128px">Quality</th>
      </tr>
    </thead>
    <tbody>
      <tr><td class="row-head">Content type</td><td>Example one</td><td>3</td><td>10</td><td>New</td><td>15%</td></tr>
      <tr><td class="row-head">Content type</td><td>Example two</td><td>6</td><td>45</td><td>New</td><td>60%</td></tr>
      <tr><td class="row-head">Content type</td><td>Example three</td><td>6</td><td>67</td><td>New</td><td>67%</td></tr>
      <tr><td class="row-head">Content type</td><td>Example four</td><td>9</td><td>94</td><td>New</td><td>22%</td></tr>
      <tr><td class="row-head">Content type</td><td>Example five</td><td>2</td><td>50</td><td>New</td><td>15%</td></tr>
      <tr><td class="row-head">Content type</td><td>Example six</td><td>1</td><td>90</td><td>New</td><td>09%</td></tr>
      <tr><td class="row-head">Content type</td><td>Example seven</td><td>5</td><td>31</td><td>New</td><td>10%</td></tr>
    </tbody>
  </table>

  <footer class="abs footer">www.yourwebsite.com &nbsp;|&nbsp; your address, location, street &nbsp;|&nbsp; +1 234 567 890 &nbsp;|&nbsp; your@email.com</footer>
</div>
</body>
</html>
```